PowerPoint Template Briefing for VARDUL

Create a professional, consistent PowerPoint template in 16:9 format that adheres to VARDUL's corporate identity guidelines. This template will be used regularly for client presentations, project proposals, and internal communications.

Template Requirements
- Format: 16:9 widescreen format for modern display compatibility
- Master slides to include:
- - Title slide with prominent logo placement
- - Section divider slides
- - Content slides with various layouts (text only, text with images, comparison layouts)
- - Data presentation slides (charts, tables, graphs)
- - Quote/testimonial slide
- - Contact/closing slide

Brand Elements Integration
- Logo placement: Consistent positioning on all slides (preferably top left or bottom right)
- Use both logo variations appropriately (text under icon for title slides, text right of icon for content slides)
- Color scheme: Implement the VARDUL color palette throughout:
- - Primary Dark Gray (#404040) for main text and headers
- - Primary Blue (#295F7C) for accents and highlights
- - Highlight Blue (#3B8AB4) for call-outs and emphasis
- Typography: Montserrat font family exclusively, with appropriate size hierarchy:
- - Slide titles: Montserrat Bold
- - Headings: Montserrat SemiBold
- - Body text: Montserrat Regular
- - Captions/footnotes: Montserrat Light

Design Elements
- Clean, minimalist design with ample white space
- Subtle background elements that evoke global connectivity and time zones
- Modern, professional look aligned with IT industry standards
- Consistent footer with slide numbers and optional space for confidentiality notices
- Custom bullet points and dividers using brand colors

Technical Specifications
- Compatible with PowerPoint 2016 and newer versions
- Embedded Montserrat font or fallback instructions
- Editable text boxes and image placeholders
- Properly set up slide masters and layouts
- Optimized file size for easy sharing

Deliverables
- .POTX template file
- Brief usage guidelines for the template
- Sample slides demonstrating various layouts and proper usage

This template should serve as the foundation for all VARDUL presentations, ensuring brand consistency while providing flexibility for various content needs.undefined

```html
<!DOCTYPE html>
<html lang="en">
<head>
<meta charset="utf-8">
<title>VARDUL Presentation Template</title>
<link href="https://fonts.googleapis.com/css2?family=Montserrat:wght@300;400;500;600;700&family=Poppins:ital,wght@0,300;0,400;0,500;0,600;0,700;1,300;1,400&display=swap" rel="stylesheet">
<style>
  :root{
    --bg-top:#f1f1f2;
    --bg-bottom:#e7e7e9;
    --ink:#404040;
    --brand:#295F7C;
    --highlight:#3B8AB4;
    --navy:#2c3a55;
    --title-blue:#2657b5;
    --tile-blue:#2f6f96;
    --soft-blue:#a9cdd8;
    --sand:#f1dec4;
    --charcoal:#3b3b3d;
    --muted:#8a8f99;
    --line:#dfe3ea;
    --panel:#eef2fa;
  }
  *{box-sizing:border-box;margin:0;padding:0}
  html,body{width:1185px;height:1200px;overflow:hidden}
  body{position:relative;font-family:"Poppins",sans-serif;color:var(--ink);
    background:linear-gradient(var(--bg-top) 0 410px,var(--bg-bottom) 410px 100%)}
  .abs{position:absolute}

  /* hero brand */
  .hero-brand{position:absolute;left:0;top:88px;width:1185px;display:flex;flex-direction:column;align-items:center;gap:14px}
  .hero-brand .ring{width:82px;height:82px;border:8px solid var(--ink);border-radius:50%}
  .hero-brand .name{font:600 44px "Montserrat",sans-serif;color:var(--brand);letter-spacing:1px}

  /* slides */
  .slide{position:absolute;width:332px;height:187px;background:#fff;box-shadow:0 3px 8px rgba(0,0,0,.14);overflow:hidden}
  .col-1{left:71px}.col-2{left:424px}.col-3{left:777px}
  .row-1{top:288px}.row-2{top:499px}.row-3{top:709px}.row-4{top:924px}

  .brand-mini{position:absolute;width:44px;display:flex;flex-direction:column;align-items:center;gap:2px}
  .brand-mini .ring{width:11px;height:11px;border:1.6px solid var(--ink);border-radius:50%}
  .brand-mini .name{font:500 8.5px "Montserrat",sans-serif;color:var(--brand);letter-spacing:.3px}

  .slide-title{position:absolute;left:22px;top:28px;font-weight:600;font-size:12px;color:var(--ink);white-space:nowrap}
  .slide-title .accent{color:var(--title-blue)}
  .year{position:absolute;font-size:4.5px;color:var(--muted)}
  .tiny{position:absolute;font-size:3.6px;line-height:1.45;color:var(--muted)}
  .tiny.italic{font-style:italic}
  .label{position:absolute;font-size:4.4px;font-weight:600;color:var(--ink);white-space:nowrap}
  .web{position:absolute;font-size:3.8px;letter-spacing:1.2px;color:var(--muted)}
  .photo{position:absolute}
  .dots{position:absolute;background-image:radial-gradient(#cfd5de 0.7px,transparent 0.8px);background-size:5px 5px}
  .bullets{position:absolute;list-style:none;font-size:3.6px;line-height:1.5;color:var(--muted)}
  .bullets li::before{content:"✓ ";color:var(--ink)}

  /* title slide */
  .title-band{left:0;top:0;width:96px;height:187px;background:var(--navy)}
  .title-name{left:148px;top:62px;font:300 31px "Montserrat",sans-serif;color:#2a2d33;letter-spacing:1px}
  .win-dots{left:22px;top:16px;display:flex;gap:3px}
  .win-dots i{width:5px;height:5px;border:0.8px solid #c8cfdb;border-radius:50%}

  /* market trends */
  .trend-item{position:absolute;left:215px;display:flex;gap:8px}
  .trend-item .icon{width:18px;height:18px;display:flex;align-items:center;justify-content:center}
  .trend-item .icon i{width:7px;height:7px;border:1px solid #fff;border-radius:1px}
  .trend-item .label,.trend-item .tiny{position:static}

  /* validation */
  .val-icon{position:absolute;width:15px;height:15px;border-radius:50%;display:flex;align-items:center;justify-content:center}
  .val-icon i{width:5px;height:5px;border:1px solid #fff;border-radius:50%}
  .val-pct{position:absolute;font-size:6px;font-weight:600;color:var(--ink)}
  .right{text-align:right}

  /* intro */
  .intro-block{left:0;top:0;width:125px;height:120px;background:var(--navy)}
  .intro-heading{left:22px;top:29px;font-size:11.5px;font-weight:600;color:#fff}
  .vline{left:189px;top:0;width:0.7px;height:56px;background:#cfd5de}

  .panel-list{left:170px;top:23px;width:70px;height:71px;background:var(--navy);padding:40px 0 0 6px;list-style:none;font-size:3.6px;line-height:1.8;color:#fff}
  .panel-list li::before{content:"› "}
  .stat-block{left:240px;top:74px;width:71px;height:91px;background:var(--tile-blue);text-align:center;color:#fff;padding-top:13px}
  .stat-block b{display:block;font-size:8px;font-weight:600}
  .stat-block span{display:block;font-size:3.8px;font-weight:600;margin-top:4px}
  .stat-block small{display:block;font-size:3px;margin-top:3px;opacity:.8;padding:0 8px}

  /* goals */
  .goal-card{position:absolute;width:69px;height:66px;border:0.8px solid var(--line);background:#fff;text-align:center;padding-top:9px}
  .goal-card .glyph{width:7px;height:7px;border:1px solid var(--highlight);border-radius:50%;margin:0 auto 5px}
  .goal-card .gl{font-size:4px;font-weight:600;color:var(--ink)}
  .goal-card .gt{font-size:3.1px;line-height:1.45;color:var(--muted);margin-top:3px;padding:0 6px}
  .goal-card.blue{background:var(--tile-blue);border-color:var(--tile-blue)}
  .goal-card.navy{background:var(--navy);border-color:var(--navy)}
  .goal-card.blue .gl,.goal-card.navy .gl,.goal-card.blue .gt,.goal-card.navy .gt{color:#fff}
  .goal-card.blue .glyph{border-color:#fff;border-radius:1px}
  .goal-card .big{font-size:8px;font-weight:600;color:#fff;margin-bottom:3px}

  /* strengths */
  .node{position:absolute;width:63px;height:16px;border:0.8px solid var(--line);background:#fff;font-size:4.2px;font-weight:600;color:var(--ink);display:flex;align-items:center;justify-content:center}
  .node.blue{background:var(--tile-blue);color:#fff;border-color:var(--tile-blue)}
  .node.navy{background:var(--navy);color:#fff;border-color:var(--navy)}

  /* key figures */
  .figure{position:absolute;top:77px;width:65px;height:44px;border:1px solid #d6dbe3;border-radius:2px;text-align:center;padding-top:7px}
  .figure .glyph{width:8px;height:7px;border:1px solid currentColor;border-radius:2px;margin:0 auto 4px}
  .figure b{font-size:10px;font-weight:500}
  .figure.blue{background:var(--tile-blue);border:1.4px solid var(--title-blue);color:#fff}
  .figure.navy{background:var(--navy);border-color:var(--navy);color:#fff}
  .figure.plain{color:var(--ink)}

  /* team leaders */
  .dark{background:var(--charcoal)}
  .dark .slide-title{color:#fff}
  .dark .slide-title .accent{color:var(--tile-blue)}
  .dark .tiny,.dark .web,.dark .bullets{color:#c9cbd0}
  .dark .label{color:#fff}
  .leader{position:absolute;top:65px;width:60px;text-align:center}
  .leader .portrait{width:36px;height:36px;margin:0 auto;border-radius:3px}
  .leader .nm{font-size:5px;color:#fff;margin-top:11px}
  .badge{display:inline-block;font-size:3.2px;padding:1px 5px;border-radius:4px;color:#fff;background:var(--title-blue)}
  .badge.navy{background:var(--navy)}
  .badge.outline{background:#fff;color:var(--ink);border:0.6px solid var(--line)}
  .badge.grey{background:#555;color:#fff}

  /* team member */
  .member{position:absolute;top:68px;width:64px;text-align:center}
  .member .avatar{width:34px;height:34px;border-radius:50%;margin:0 auto}
  .member .nm{font-size:5px;color:var(--ink);margin:8px 0 3px}
  .member .tiny{position:static;margin-top:4px}

  /* objectives */
  .obj-tile{position:absolute;top:67px;width:47px;height:48px;font-size:3.6px;color:#fff;text-align:center;padding-top:12px}
  .obj-tile .glyph{width:7px;height:7px;border:1px solid currentColor;border-radius:50%;margin:0 auto 6px}
  .obj-pct{position:absolute;top:129px;width:47px;text-align:center;font-size:6.5px;font-weight:600;color:var(--ink)}
  .obj-note{position:absolute;top:145px;width:47px;text-align:center;font-size:3px;line-height:1.4;color:var(--muted)}
  .btn{position:absolute;left:22px;top:153px;width:37px;height:11px;border-radius:6px;background:var(--navy);color:#fff;font-size:3.5px;display:flex;align-items:center;justify-content:center}

  .obj-panel{left:122px;top:60px;width:211px;height:127px;background:var(--panel)}
  .metric{position:absolute;top:88px;width:50px;text-align:center}
  .metric .dot{width:14px;height:14px;border-radius:50%;margin:0 auto;display:flex;align-items:center;justify-content:center}
  .metric .dot i{width:5px;height:5px;border:1px solid #fff;border-radius:1px}
  .metric .ml{font-size:3.6px;color:var(--ink);margin-top:7px}
  .metric b{display:block;font-size:7px;font-weight:600;color:var(--ink);margin-top:5px}
  .metric .tiny{position:static;margin-top:5px}
  .point{position:absolute;left:28px}
  .point .label{position:static}
  .point .label::before{content:"";display:inline-block;width:2.5px;height:2.5px;border-radius:50%;background:var(--title-blue);margin-right:5px;vertical-align:middle}
  .point .tiny{position:static;padding-left:8px;margin-top:2px;width:80px}
</style>
</head>
<body>

<header class="hero-brand">
  <div class="ring"></div>
  <div class="name">VARDUL</div>
</header>

<!-- Title slide -->
<section class="slide col-1 row-1">
  <div class="abs title-band"></div>
  <div class="abs win-dots"><i></i><i></i><i></i></div>
  <div class="photo" role="img" aria-label="Photo of a modern glass office building facade" style="left:22px;top:36px;width:97px;height:134px;background:linear-gradient(135deg,#8d93a6,#dfe3ec 45%,#6c7287)"></div>
  <div class="brand-mini" style="left:246px;top:18px"><div class="ring"></div><div class="name">VARDUL</div></div>
  <div class="year" style="left:303px;top:15px">2025</div>
  <div class="abs title-name">VARDUL</div>
  <div class="tiny italic" style="left:152px;top:107px;width:110px">Short notes about the company and its services, written in a calm voice.</div>
  <div class="tiny" style="left:152px;top:125px">Date: 07/06/25</div>
  <div class="dots" style="left:273px;top:152px;width:46px;height:19px"></div>
  <div class="web" style="left:152px;top:168px">www.vardul-deck.net</div>
</section>

<!-- Market Trends -->
<section class="slide col-2 row-1">
  <div class="slide-title"><span class="accent">Market</span> Trends</div>
  <div class="brand-mini" style="left:262px;top:18px"><div class="ring"></div><div class="name">VARDUL</div></div>
  <svg class="abs" style="left:0;top:0" width="200" height="187" viewBox="0 0 200 187">
    <g stroke="#eceff3" stroke-width="0.5">
      <line x1="30" y1="79" x2="170" y2="79"/><line x1="30" y1="91" x2="170" y2="91"/>
      <line x1="30" y1="103" x2="170" y2="103"/><line x1="30" y1="115" x2="170" y2="115"/>
      <line x1="30" y1="127" x2="170" y2="127"/><line x1="30" y1="139" x2="170" y2="139"/>
      <line x1="30" y1="151" x2="170" y2="151"/><line x1="30" y1="163" x2="170" y2="163"/>
    </g>
    <g font-size="3" fill="#8a8f99" font-family="Poppins,sans-serif">
      <text x="24" y="80">14</text><text x="24" y="92">12</text><text x="24" y="104">10</text>
      <text x="25" y="116">8</text><text x="25" y="128">6</text><text x="25" y="140">4</text>
      <text x="25" y="152">2</text><text x="25" y="164">0</text>
      <text x="44" y="170">2021</text><text x="78" y="170">2022</text><text x="113" y="170">2023</text><text x="147" y="170">2024</text>
    </g>
    <g>
      <rect x="46" y="112" width="5" height="10" fill="#a9cdd8"/><rect x="46" y="122" width="5" height="4" fill="#2f6f96"/><rect x="46" y="126" width="5" height="37" fill="#2c3a55"/>
      <rect x="80" y="110" width="5" height="11" fill="#a9cdd8"/><rect x="80" y="121" width="5" height="10" fill="#2f6f96"/><rect x="80" y="131" width="5" height="32" fill="#2c3a55"/>
      <rect x="115" y="114" width="5" height="16" fill="#a9cdd8"/><rect x="115" y="130" width="5" height="10" fill="#2f6f96"/><rect x="115" y="140" width="5" height="23" fill="#2c3a55"/>
      <rect x="149" y="91" width="5" height="17" fill="#a9cdd8"/><rect x="149" y="108" width="5" height="18" fill="#2f6f96"/><rect x="149" y="126" width="5" height="37" fill="#2c3a55"/>
    </g>
  </svg>
  <div class="trend-item" style="top:54px"><div class="icon" style="background:var(--navy)"><i></i></div><div><div class="label">Environment</div><div class="tiny">Notes on climate rules and<br>their effect on buyers.</div></div></div>
  <div class="trend-item" style="top:87px"><div class="icon" style="background:var(--tile-blue)"><i></i></div><div><div class="label">Legal</div><div class="tiny">Notes on new laws and<br>their effect on trade.</div></div></div>
  <div class="trend-item" style="top:119px"><div class="icon" style="background:var(--soft-blue)"><i></i></div><div><div class="label">Technology</div><div class="tiny">Notes on new tools and<br>their effect on teams.</div></div></div>
  <div class="trend-item" style="top:151px"><div class="icon" style="background:var(--sand)"><i></i></div><div><div class="label">Economy</div><div class="tiny">Notes on prices and<br>their effect on demand.</div></div></div>
</section>

<!-- Market Validation -->
<section class="slide col-3 row-1">
  <div class="slide-title" style="left:112px;top:25px"><span class="accent">Market</span> Validation</div>
  <div class="brand-mini" style="left:278px;top:18px"><div class="ring"></div><div class="name">VARDUL</div></div>
  <svg class="abs" style="left:124px;top:77px" width="86" height="86" viewBox="0 0 86 86">
    <g transform="rotate(-90 43 43)" fill="none" stroke-width="5">
      <circle cx="43" cy="43" r="40" stroke="#e4e6ea"/>
      <circle cx="43" cy="43" r="40" stroke="#2c3a55" stroke-dasharray="135 117"/>
      <circle cx="43" cy="43" r="40" stroke="#2f6f96" stroke-dasharray="28 224" stroke-dashoffset="-135"/>
      <circle cx="43" cy="43" r="40" stroke="#a9cdd8" stroke-dasharray="42 210" stroke-dashoffset="-163"/>
    </g>
    <text x="43" y="45" text-anchor="middle" font-family="Poppins,sans-serif" font-size="11" fill="#2c3a55">8<tspan fill="#2657b5">M</tspan></text>
    <text x="43" y="54" text-anchor="middle" font-family="Poppins,sans-serif" font-size="3.6" fill="#8a8f99">Total</text>
  </svg>
  <div class="val-icon" style="left:26px;top:75px;background:#e9ebef"><i style="border-color:#2c3a55"></i></div>
  <div class="val-pct" style="left:52px;top:72px">40%</div>
  <div class="label" style="left:52px;top:82px;font-weight:400">First Advantages</div>
  <div class="tiny" style="left:52px;top:89px;width:58px">A short line about the first gain and how it helps.</div>
  <div class="val-icon" style="left:26px;top:133px;background:var(--soft-blue)"><i style="border-color:#2f6f96"></i></div>
  <div class="val-pct" style="left:52px;top:130px">37%</div>
  <div class="label" style="left:52px;top:140px;font-weight:400">Second Advantages</div>
  <div class="tiny" style="left:52px;top:147px;width:58px">A short line about the second gain and how it helps.</div>
  <div class="val-icon" style="left:294px;top:75px;background:var(--navy)"><i></i></div>
  <div class="val-pct right" style="left:258px;top:72px;width:26px">78%</div>
  <div class="label right" style="left:224px;top:82px;width:60px;font-weight:400">Three Advantages</div>
  <div class="tiny right" style="left:226px;top:89px;width:58px">A short line about the third gain and how it helps.</div>
  <div class="val-icon" style="left:294px;top:133px;background:var(--title-blue)"><i></i></div>
  <div class="val-pct right" style="left:258px;top:130px;width:26px">15%</div>
  <div class="label right" style="left:224px;top:140px;width:60px;font-weight:400">Other Advantages</div>
  <div class="tiny right" style="left:226px;top:147px;width:58px">A short line about other gains and how they help.</div>
</section>

<!-- Introduction -->
<section class="slide col-1 row-2">
  <div class="abs intro-block"></div>
  <div class="abs intro-heading">Introduction</div>
  <div class="photo" role="img" aria-label="Photo of a person working at a laptop on a desk" style="left:72px;top:75px;width:70px;height:92px;background:linear-gradient(160deg,#d9dde3,#b9c0c9 55%,#5b6270)"></div>
  <div class="abs vline"></div>
  <div class="brand-mini" style="left:246px;top:10px"><div class="ring"></div><div class="name">VARDUL</div></div>
  <div class="year" style="left:303px;top:15px">2025</div>
  <div class="label" style="left:190px;top:67px;line-height:1.4">Best Option To Start<br>Your Business</div>
  <div class="tiny italic" style="left:190px;top:92px;width:120px">A few words on why this plan suits a young firm and how it can grow step by step.</div>
  <ul class="bullets" style="left:190px;top:124px;width:120px">
    <li>Clear goals set for each team member</li>
    <li>Simple tools that save time every day</li>
    <li>Steady support from a trusted partner</li>
    <li>Fair prices that fit a small budget</li>
    <li>Room to grow when needs change</li>
  </ul>
  <div class="dots" style="left:37px;top:153px;width:38px;height:16px"></div>
</section>

<!-- Intro -->
<section class="slide col-2 row-2">
  <div class="slide-title" style="top:27px">Intro</div>
  <div class="label" style="left:22px;top:66px">Summary Purpose Profile</div>
  <div class="tiny italic" style="left:22px;top:78px;width:120px">A brief summary of our purpose and the people we serve across many regions.</div>
  <div class="tiny" style="left:22px;top:100px;width:120px">We build clear and useful systems for clients in many fields, with care for each detail and a focus on lasting value.</div>
  <div class="tiny" style="left:22px;top:122px;width:120px">Our teams work across time zones to keep projects moving and to share results with partners quickly.</div>
  <div class="web" style="left:22px;top:164px">www.vardul-deck.net</div>
  <ul class="abs panel-list"><li>History</li><li>Industry Experience</li><li>Product Range</li><li>Services</li></ul>
  <div class="photo" role="img" aria-label="Photo of a curved modern building against the sky" style="left:240px;top:23px;width:71px;height:51px;background:linear-gradient(180deg,#e6ecf2,#9aa6b4)"></div>
  <div class="abs stat-block"><b>94%</b><span>Partner Service</span><small>Notes on how we help partners</small></div>
  <div class="photo" role="img" aria-label="Photo of colleagues meeting around a table with coffee" style="left:170px;top:94px;width:70px;height:71px;background:linear-gradient(160deg,#4f6a86,#c9d3dc 60%,#3c4756)"></div>
</section>

<!-- Our Goals -->
<section class="slide col-3 row-2">
  <div class="slide-title"><span class="accent">Our</span> Goals</div>
  <div class="label" style="left:22px;top:62px">Our goals and objectives</div>
  <div class="tiny italic" style="left:22px;top:72px;width:120px">We aim to serve clients well and to grow with them in every market we enter.</div>
  <div class="brand-mini" style="left:15px;top:103px"><div class="ring"></div><div class="name">VARDUL</div></div>
  <div class="dots" style="left:22px;top:157px;width:14px;height:5px"></div>
  <div class="goal-card blue" style="left:171px;top:26px"><div class="glyph"></div><div class="gl">Reliability</div><div class="gt">We keep our word and deliver on time for all.</div></div>
  <div class="goal-card" style="left:244px;top:26px"><div class="glyph"></div><div class="gl">Happy Customers</div><div class="gt">We listen closely and act on what we hear.</div></div>
  <div class="goal-card" style="left:98px;top:95px"><div class="glyph"></div><div class="gl">Superior Quality</div><div class="gt">We test each piece of work with great care.</div></div>
  <div class="goal-card" style="left:171px;top:95px"><div class="glyph"></div><div class="gl">Prevalence</div><div class="gt">We reach more places year after year.</div></div>
  <div class="goal-card navy" style="left:244px;top:95px"><div class="big">97%</div><div class="gl">Partner Services</div><div class="gt">Most partners renew with us each year.</div></div>
</section>

<!-- Our Strengths -->
<section class="slide col-1 row-3">
  <div class="slide-title"><span class="accent">Our</span> Strengths</div>
  <div class="brand-mini" style="left:246px;top:12px"><div class="ring"></div><div class="name">VARDUL</div></div>
  <div class="label" style="left:22px;top:61px">Our achievements</div>
  <div class="tiny italic" style="left:22px;top:71px;width:80px">A look at what our teams have done in recent years.</div>
  <svg class="abs" style="left:0;top:0" width="332" height="187">
    <g stroke="#dfe3ea" stroke-width="0.7">
      <line x1="168" y1="58" x2="168" y2="76"/><line x1="168" y1="92" x2="168" y2="109"/><line x1="168" y1="125" x2="168" y2="142"/>
      <line x1="104" y1="117" x2="137" y2="117"/><line x1="200" y1="117" x2="235" y2="117"/>
    </g>
  </svg>
  <div class="node blue" style="left:137px;top:42px">Focus Strengths</div>
  <div class="node" style="left:137px;top:76px">Communications</div>
  <div class="node navy" style="left:137px;top:109px">Personal Split</div>
  <div class="node" style="left:137px;top:142px">Teamwork</div>
  <div class="node" style="left:41px;top:109px">Thinking</div>
  <div class="node" style="left:235px;top:109px">Problem Solving</div>
  <div class="tiny" style="left:235px;top:60px;width:65px">We share ideas openly and agree on the next step together as one team.</div>
  <div class="tiny" style="left:22px;top:152px;width:60px">We think ahead and plan each task with care.</div>
  <div class="tiny" style="left:235px;top:159px;width:60px">We solve hard issues fast and fairly.</div>
</section>

<!-- Key Figures -->
<section class="slide col-2 row-3">
  <div class="slide-title"><span class="accent">Key</span> Figures</div>
  <div class="tiny italic" style="left:194px;top:25px;width:115px">The numbers below show how far we have come and where we plan to go next.</div>
  <div class="figure plain" style="left:22px"><div class="glyph"></div><b>28</b></div>
  <div class="figure blue" style="left:97px"><div class="glyph"></div><b>245k</b></div>
  <div class="figure plain" style="left:172px;border-color:#eceff3"><div class="glyph"></div><b>945</b></div>
  <div class="figure navy" style="left:246px"><div class="glyph"></div><b>7M</b></div>
  <ul class="bullets" style="left:22px;top:138px;width:62px"><li>Years of steady work for clients in many fields</li></ul>
  <ul class="bullets" style="left:97px;top:138px;width:62px"><li>Happy users who rely on our tools every day</li></ul>
  <ul class="bullets" style="left:172px;top:138px;width:62px"><li>Projects done on time and within budget</li></ul>
  <ul class="bullets" style="left:246px;top:138px;width:62px"><li>Total revenue earned in the past year</li></ul>
</section>

<!-- Team Leaders -->
<section class="slide dark col-3 row-3">
  <div class="slide-title"><span class="accent">Team</span> Leaders</div>
  <div class="label" style="left:22px;top:73px">Team Members found in : Leaders</div>
  <div class="tiny italic" style="left:22px;top:82px;width:95px">The people who guide our teams and set the course.</div>
  <div class="tiny" style="left:22px;top:98px;width:95px">Our leaders bring years of skill to each project and help every member do their best work.</div>
  <div class="web" style="left:22px;top:164px">www.vardul-deck.net</div>
  <div class="leader" style="left:145px"><div class="portrait" role="img" aria-label="Portrait photo of a team leader" style="background:linear-gradient(180deg,#e8e4df,#a58f7c)"></div><div class="nm">Your Name</div><span class="badge">CEO</span></div>
  <div class="leader" style="left:231px"><div class="portrait" role="img" aria-label="Portrait photo of a team leader" style="background:linear-gradient(180deg,#d8c3a7,#7a5c45)"></div><div class="nm">Your Name</div><span class="badge grey">Product</span></div>
  <ul class="bullets" style="left:150px;top:137px;width:60px"><li>Leads the firm and sets long term goals</li></ul>
  <ul class="bullets" style="left:235px;top:137px;width:60px"><li>Shapes each product from idea to launch</li></ul>
</section>

<!-- Team member -->
<section class="slide col-1 row-4">
  <div class="brand-mini" style="left:33px;top:12px"><div class="ring"></div><div class="name">VARDUL</div></div>
  <div class="slide-title" style="left:121px;top:17px"><span class="accent">Team</span> member</div>
  <div class="tiny italic" style="left:88px;top:35px;width:160px">Meet the people behind our work and learn what each one brings.</div>
  <div class="member" style="left:20px"><div class="avatar" role="img" aria-label="Portrait photo of a team member" style="background:linear-gradient(180deg,#ece6df,#c7ad92)"></div><div class="nm">Elian Moross</div><span class="badge">Business</span><div class="tiny">Guides new deals and client ties.</div></div>
  <div class="member" style="left:97px"><div class="avatar" role="img" aria-label="Portrait photo of a team member" style="background:linear-gradient(180deg,#cfcfcf,#3a3a3a)"></div><div class="nm">Elian Moross</div><span class="badge outline">Marketing</span><div class="tiny">Shares our story with the world.</div></div>
  <div class="member" style="left:174px"><div class="avatar" role="img" aria-label="Portrait photo of a team member" style="background:linear-gradient(180deg,#f0ece8,#9b7b66)"></div><div class="nm">Elian Moross</div><span class="badge navy">Social</span><div class="tiny">Runs our online channels daily.</div></div>
  <div class="member" style="left:251px"><div class="avatar" role="img" aria-label="Portrait photo of a team member" style="background:linear-gradient(180deg,#2a2a2a,#6d5a4c)"></div><div class="nm">Elian Moross</div><span class="badge outline">Plan</span><div class="tiny">Keeps every plan on track.</div></div>
</section>

<!-- Our Objectives -->
<section class="slide col-2 row-4">
  <div class="slide-title"><span class="accent">Our</span> Objectives</div>
  <div class="tiny italic" style="left:192px;top:25px;width:118px">These targets guide our choices and show what we want to reach this year.</div>
  <ul class="bullets" style="left:22px;top:69px;width:62px">
    <li>Grow profit with smart and careful spending</li>
    <li>Serve clients faster with better tools</li>
    <li>Stay fair in all we do</li>
  </ul>
  <div class="btn">VISIT US</div>
  <div class="obj-tile" style="left:100px;background:var(--navy)"><div class="glyph"></div>Profitability</div>
  <div class="obj-tile" style="left:153px;background:#4f77b5"><div class="glyph"></div>Customer Service</div>
  <div class="obj-tile" style="left:206px;background:var(--soft-blue);color:#2c3a55"><div class="glyph"></div>Growth</div>
  <div class="obj-tile" style="left:260px;background:var(--sand);color:#2c3a55"><div class="glyph"></div>Efficiency</div>
  <div class="obj-pct" style="left:100px">10%</div><div class="obj-pct" style="left:153px">20%</div>
  <div class="obj-pct" style="left:206px">40%</div><div class="obj-pct" style="left:260px">60%</div>
  <div class="obj-note" style="left:100px">More profit from each new client</div>
  <div class="obj-note" style="left:153px">Quicker replies to every request</div>
  <div class="obj-note" style="left:206px">New markets opened this year</div>
  <div class="obj-note" style="left:260px">Less waste in daily tasks</div>
</section>

<!-- Objectives -->
<section class="slide col-3 row-4">
  <div class="slide-title" style="color:#2a2d33">Objectives</div>
  <div class="tiny italic" style="left:192px;top:25px;width:118px">These aims shape how we work and how we measure our progress.</div>
  <div class="point" style="top:60px"><div class="label">Be Great At Things</div><div class="tiny">Aim high in each task and learn from every result.</div></div>
  <div class="point" style="top:96px"><div class="label">Not Suck At Things</div><div class="tiny">Fix weak spots early and keep the bar high.</div></div>
  <div class="point" style="top:131px"><div class="label">Live Honestly Run Out Of<br>Things To Say</div><div class="tiny">Speak plainly and keep each promise made.</div></div>
  <div class="abs obj-panel"></div>
  <div class="metric" style="left:138px"><div class="dot" style="background:var(--navy)"><i></i></div><div class="ml">Customer Service</div><b>20%</b><div class="tiny">Faster help for every client</div></div>
  <div class="metric" style="left:202px"><div class="dot" style="background:var(--title-blue)"><i></i></div><div class="ml">Growth</div><b>40%</b><div class="tiny">More reach in new regions</div></div>
  <div class="metric" style="left:264px"><div class="dot" style="background:var(--soft-blue)"><i style="border-color:#2c3a55"></i></div><div class="ml">Efficiency</div><b>60%</b><div class="tiny">Less time lost each week</div></div>
</section>

</body>
</html>
```